Printing Company needs Website

PLEASE REVIEW ALL IMAGES, I HAVE INCLUDED A WEBSITE MOCKUP IDEA AND LOGO FILES IN THESE IMAGES.

Vexo-Marks Provides printing services to multiple businesses. We Focus on 4 main markets. Signage (Signs, Banners, Wraps, Custom graphics), Printing (flyers, brochures, business cards, Postcards), Apparel (printed shirts, hoodies, sweatshirts), Promotional Products (mugs, golf balls, brimo cans, pens), We try to sell ourselves on total brand imaging, our slogan is "Print Anything." because we want to be able to provide any type of printing to our customers. Consumer targeting should be targeted towards small business, and wholesale targeting should be geared toward, merchandising, branding, marketing, design, signage, apparel, embroidery, and printing groups. WE DO OFFER DESIGN SERVICES, I have attached one lindmoor council logo design as an example.

I need a website designed both for wholesale and consumer based people. Wholesale customers would have their own login and consumers would also have their own.
I need there to be an online designer software (possibly java) built in so that the customer can order their product or upload their artwork online to see the proof for approval. There will need to be an commence setup, and I do have a quillo account if that helps. Shipping must be auto calculated at the time of ordering. I would Like to make it to where when customer orders a product if it is outside of the dimensions requested on the site that the customer is warned of clipping or skewing.

I will be working closely aside the designer I pick to aid in the uploading and configuration of pricing structure, weight, and imagery if selected. This will be a lengthy project, and I will be willing to pay for the additional help so long as you are completely aware of the needs, Happy designing!!
Updates

I love all of the designs so far everyone! I will be reviewing PLEASE NOTE, IF I APPROVE YOUR WEB DESIGN, I WILL WANT YOU TO COMPLETE THE ENTIRE DESIGN INCLUDING A DESIGN PROOFING SETUP FOR MY CUSTOMERS INTEGRATED IN AS I HAVE STATED IN THE ORIGINAL STATEMENT. PLEASE ASK QUESTIONS IF YOU DON'T UNDERSTAND!

Target Market(s)

Small Business, School Athletics, Merchandising groups, Branding Groups, Larger Printers, Sign makers, Embroidery shops, Screen Printing Shops

Industry/Entity Type

It Company

Font styles to use
Sans Serif

Colors
000000
1b1b1b
757575
ec1f27

Requirements
Must have
• Built in design setup to each product with sizing, Ability to add pre-designed templates, .pdf print ready files after upload, Wholesale account, or Business accounts all with different pricing structures, Must be willing to aid in setup of all products and services (willing pay additional for setup costs.)
Nice to have
• SEO Optimization, targeting specific groups listed, automatic ordering to outsource vendors straight from site listing drop ship location if need be.

```html
<!DOCTYPE html>
<html lang="en">
<head>
<meta charset="utf-8">
<title>Vexo-Marks — Print Anything</title>
<link href="https://fonts.googleapis.com/css2?family=Lato:wght@100;300&family=Open+Sans:wght@300;400;500;600&display=swap" rel="stylesheet">
<style>
  :root {
    --black: #000000;
    --charcoal: #1b1b1b;
    --base: #141414;
    --grey: #757575;
    --muted: #9a9a9a;
    --red: #ec1f27;
    --white: #ffffff;
    --line: #3a3a3a;
  }
  * { margin: 0; padding: 0; box-sizing: border-box; }
  html, body { width: 1200px; height: 1036px; overflow: hidden; background: var(--charcoal); }
  body { position: relative; font-family: "Open Sans", Arial, sans-serif; color: var(--white); }

  .hero {
    position: absolute; left: 0; top: 0; width: 1200px; height: 641px; z-index: 0;
    background:
      linear-gradient(180deg, #2f62b0 0%, #5a86c4 22%, #9fb3cf 30%, #b9b3a6 38%, #8f8a82 52%, #3d3d3f 62%, #545a4a 78%, #7b7a63 90%, #4a4c3c 100%);
  }
  .hero-shade {
    position: absolute; inset: 0;
    background: linear-gradient(90deg, rgba(0,0,0,0.15) 0%, rgba(0,0,0,0) 40%, rgba(0,0,0,0.1) 100%);
  }

  .main-nav { position: absolute; top: 0; left: 0; width: 1200px; height: 130px; z-index: 3; }
  .main-nav a {
    position: absolute; top: 69px; font-size: 11px; font-weight: 500;
    color: var(--white); text-decoration: none; letter-spacing: 0.1px;
  }
  .brand { position: absolute; left: 478px; top: 46px; width: 250px; text-align: center; }
  .brand-name {
    font-family: "Open Sans", Arial, sans-serif; font-weight: 600; font-size: 36px;
    color: var(--white); letter-spacing: 0.5px; line-height: 1;
  }
  .brand-tag { position: absolute; left: 160px; top: 50px; font-size: 12px; color: var(--white); }

  .slider-dots { position: absolute; left: 1154px; top: 258px; z-index: 3; }
  .slider-dots span {
    display: block; width: 8px; height: 8px; border-radius: 50%;
    background: rgba(255,255,255,0.85); margin-bottom: 16px;
  }
  .slider-dots span.active { background: transparent; border: 1px solid rgba(255,255,255,0.7); }

  .hero-title {
    position: absolute; left: 36px; top: 366px; z-index: 3; font-family: "Lato", Arial, sans-serif;
    font-weight: 100; font-size: 88px; line-height: 1; color: var(--white);
    text-shadow: 0 1px 3px rgba(0,0,0,0.35);
  }

  .markets { position: absolute; inset: 0; z-index: 5; pointer-events: none; }
  .market-card {
    position: absolute; width: 268px; background: var(--red); top: 601px; height: 139px;
    padding: 24px 16px 0 32px; box-shadow: 0 8px 12px rgba(0,0,0,0.35);
  }
  .market-card.featured { top: 532px; height: 208px; padding-top: 93px; }
  .market-card h3 { font-weight: 300; font-size: 19px; line-height: 1.2; margin-bottom: 13px; white-space: nowrap; }
  .market-card .rule { width: 51px; height: 1px; background: rgba(255,255,255,0.85); margin-bottom: 12px; }
  .market-card p { font-size: 12px; line-height: 23px; white-space: nowrap; }
  .sign-icon { position: absolute; left: 65px; top: 555px; width: 58px; height: 60px; }

  .site-footer { position: absolute; left: 0; top: 641px; width: 1200px; height: 347px; background: var(--charcoal); z-index: 1; }
  .footer-col { position: absolute; top: 151px; }
  .footer-col h4 { font-weight: 300; font-size: 19px; color: var(--white); margin-bottom: 14px; }
  .footer-col p { font-size: 12px; color: var(--muted); line-height: 22px; }
  .footer-col ul { list-style: none; }
  .footer-col li { font-size: 11.5px; color: var(--muted); line-height: 24px; }
  .link-cols { display: flex; }
  .link-cols ul:first-child { width: 135px; }

  .social { display: flex; gap: 7px; margin-top: 19px; margin-left: 1px; }
  .social span { width: 34px; height: 34px; border-radius: 50%; display: block; }

  .newsletter-input {
    margin-top: 14px; width: 263px; height: 37px; border: 1px solid var(--line);
    display: flex; align-items: center; justify-content: space-between; padding: 0 10px 0 17px;
    font-size: 11.5px; color: #b5b5b5;
  }

  .legal-bar {
    position: absolute; left: 0; top: 988px; width: 1200px; height: 48px; background: var(--base);
    text-align: center; font-size: 11px; line-height: 48px; color: var(--muted); z-index: 1;
  }
</style>
</head>
<body>

<div class="hero" role="img" aria-label="Photo of a storefront restaurant building with large printed window graphics, parked cars and landscaping under a blue sky">
  <div class="hero-shade"></div>
</div>

<nav class="main-nav">
  <a style="left:82px">HOME</a>
  <a style="left:171px">SIGNAGE</a>
  <a style="left:275px">PRINTING</a>
  <a style="left:381px">DESIGN</a>
  <div class="brand">
    <div class="brand-name">Vexo-Marks</div>
    <div class="brand-tag">Print Anything.</div>
  </div>
  <a style="left:759px">PROMOTIONAL</a>
  <a style="left:886px">APPAREL</a>
  <a style="left:981px">ABOUT US</a>
  <a style="left:1084px">CONTACT US</a>
</nav>

<div class="slider-dots">
  <span class="active"></span><span></span><span></span><span></span><span class="active"></span>
</div>

<h1 class="hero-title">Print Anything</h1>

<footer class="site-footer">
  <div class="footer-col" style="left:58px">
    <h4>Follow Us</h4>
    <p>Connect with our social network</p>
    <div class="social" aria-label="Social network links">
      <span style="background:#ea4c89"></span>
      <span style="background:#3fa9e0"></span>
      <span style="background:#1c7aa8"></span>
      <span style="background:#d9262c"></span>
      <span style="background:#2a64b0"></span>
      <span style="background:#f0a21b"></span>
    </div>
  </div>

  <div class="footer-col" style="left:396px">
    <h4>Welcome</h4>
    <div class="link-cols">
      <ul><li>Home</li><li>Signage</li><li>Printing</li><li>Design</li><li>Promotional</li></ul>
      <ul><li>Apparel</li><li>About Us</li><li>Contact us</li></ul>
    </div>
  </div>

  <div class="footer-col" style="left:681px">
    <h4>Information</h4>
    <ul><li>Terms &amp; Conditions</li><li>Privacy Policy</li><li>Disclaimer</li><li>Sitemap</li></ul>
  </div>

  <div class="footer-col" style="left:896px">
    <h4>Newsletter signup</h4>
    <p>Get our recent updates through your<br>email id</p>
    <div class="newsletter-input">
      <span>Enter your email id</span>
      <svg width="20" height="10" viewBox="0 0 20 10" fill="none" stroke="#bbb" stroke-width="1.3"><path d="M0 5 h18 M14 1 l4 4 l-4 4"/></svg>
    </div>
  </div>
</footer>

<section class="markets">
  <article class="market-card featured" style="left:42px">
    <h3>Signage</h3>
    <div class="rule"></div>
    <p>Signs, Banners, Wraps, Custom<br>graphics</p>
  </article>
  <svg class="sign-icon" viewBox="0 0 58 60" fill="none" stroke="#fff" stroke-width="2.4" stroke-linejoin="round">
    <path d="M27 2 h6 v6 M27 2 v6"/>
    <path d="M6 8 h48 l4 6 l-4 6 h-48 z"/>
    <path d="M52 26 h-48 l-4 6 l4 6 h48 z"/>
    <path d="M27 20 v6 M33 20 v6 M27 38 v20 M33 38 v20"/>
  </svg>
  <article class="market-card" style="left:325px">
    <h3>Printing</h3>
    <div class="rule"></div>
    <p>Flyers, Brochures, Business cards,<br>Postcards</p>
  </article>
  <article class="market-card" style="left:608px">
    <h3>Apparel</h3>
    <div class="rule"></div>
    <p>Printed shirts, Hoodies,<br>Sweatshirts</p>
  </article>
  <article class="market-card" style="left:891px">
    <h3>Promotional Products</h3>
    <div class="rule"></div>
    <p>Mugs, Golf balls, Brimo cans,<br>Pens</p>
  </article>
</section>

<div class="legal-bar">Copyright © 2016. Vexo-Marks. All rights reserved.</div>

</body>
</html>
```